KerrLow Farm

Need a nice simple clean double sided business card that has our logo and info on:
Kerr Low Farm
Martin & Felicity Kerr Low
kerrlowfarm@mailbarn.example
Martin: 1-780-555-0148
Felicity: 1-780-555-0193
Instagram @ kerrlow_farm

Contact Information for Business Card

Martin & Felicity Kerr Low kerrlowfarm@mailbarn.example Martin: 1-780-555-0148 Felicity: 1-780-555-0193

```html
<!DOCTYPE html>
<html lang="en">
<head>
<meta charset="utf-8">
<title>Kerr Low Farm – Business Card</title>
<link rel="stylesheet" href="https://fonts.googleapis.com/css2?family=Cinzel:wght@500;600&family=Open+Sans:wght@400&family=Raleway:wght@500&display=swap">
<style>
  :root {
    --backdrop: #e6e6e6;
    --card: #f4f4f4;
    --green: #5c9e3c;
    --orange: #f0a024;
    --ink: #333333;
  }
  * { margin: 0; padding: 0; box-sizing: border-box; }
  html, body { width: 1200px; height: 960px; overflow: hidden; }
  body { background: var(--backdrop); position: relative; font-family: "Open Sans", sans-serif; }

  .card { position: absolute; background: var(--card); }
  .card-front { left: 121px; top: 340px; width: 584px; height: 333px; }
  .card-back { left: 745px; top: 190px; width: 334px; height: 583px; }

  .brand-ring {
    position: absolute; border: 4px solid var(--green); border-radius: 50%;
    display: flex; align-items: center; justify-content: center; text-align: center;
  }
  .card-front .brand-ring { left: 236px; top: 86px; width: 112px; height: 112px; }
  .card-back .brand-ring { left: 47px; top: 45px; width: 112px; height: 112px; }
  .brand-ring .ring-name {
    font-family: "Cinzel", serif; font-weight: 600; font-size: 13px; line-height: 1.25;
    color: var(--green);
  }

  .brand-name {
    position: absolute; left: 0; width: 100%; top: 196px; text-align: center;
    font-family: "Cinzel", serif; font-weight: 600; font-size: 33px; color: var(--green);
    letter-spacing: 0.2px;
  }
  .brand-tagline {
    position: absolute; left: 0; width: 100%; top: 237px; text-align: center;
    font-family: "Raleway", sans-serif; font-weight: 500; font-size: 14px;
    letter-spacing: 4.6px; color: var(--orange);
  }

  .owners {
    position: absolute; left: 48px; top: 325px;
    font-family: "Cinzel", serif; font-weight: 600; font-size: 21px; line-height: 26px;
  }
  .owners .first-names { color: var(--green); }
  .owners .surname { color: var(--orange); }

  .contact-row { position: absolute; left: 46px; width: 202px; }
  .contact-rule { display: flex; align-items: center; height: 20px; }
  .contact-rule svg { flex: none; }
  .contact-rule .line { flex: 1; height: 1.5px; background: var(--green); margin-left: 2px; }
  .contact-text { font-size: 14px; line-height: 20px; color: var(--ink); margin-left: 0; }
  .contact-text .label { color: var(--green); }
  .row-phone { top: 392px; }
  .row-mail { top: 460px; }
  .row-social { top: 509px; }
</style>
</head>
<body>
  <section class="card card-front">
    <div class="brand-ring"></div>
    <div class="brand-name">KERR LOW FARM</div>
    <div class="brand-tagline">STONE MILLED FLOUR</div>
  </section>

  <section class="card card-back">
    <div class="brand-ring"><span class="ring-name">Kerr Low<br>Farm</span></div>

    <div class="owners">
      <div class="first-names">Martin &amp; Felicity</div>
      <div class="surname">Kerr Low</div>
    </div>

    <div class="contact-row row-phone">
      <div class="contact-rule">
        <svg width="20" height="20" viewBox="0 0 20 20" aria-hidden="true">
          <circle cx="10" cy="10" r="8.8" fill="none" stroke="var(--green)" stroke-width="1.6"/>
          <rect x="7" y="4.5" width="6" height="11" rx="1" fill="none" stroke="var(--orange)" stroke-width="1.3"/>
        </svg>
        <span class="line"></span>
      </div>
      <div class="contact-text"><span class="label">Martin</span> 1-780-555-0148</div>
      <div class="contact-text"><span class="label">Felicity</span> 1-780-555-0193</div>
    </div>

    <div class="contact-row row-mail">
      <div class="contact-rule">
        <svg width="20" height="20" viewBox="0 0 20 20" aria-hidden="true">
          <circle cx="10" cy="10" r="8.8" fill="none" stroke="var(--green)" stroke-width="1.6"/>
          <rect x="5" y="6.5" width="10" height="7" fill="none" stroke="var(--orange)" stroke-width="1.3"/>
          <path d="M5 6.5 L10 10.5 L15 6.5" fill="none" stroke="var(--orange)" stroke-width="1.3"/>
        </svg>
        <span class="line"></span>
      </div>
      <div class="contact-text">kerrlowfarm@mailbarn.example</div>
    </div>

    <div class="contact-row row-social">
      <div class="contact-rule">
        <svg width="20" height="20" viewBox="0 0 20 20" aria-hidden="true">
          <circle cx="10" cy="10" r="8.8" fill="none" stroke="var(--green)" stroke-width="1.6"/>
          <circle cx="10" cy="10" r="4" fill="var(--orange)"/>
        </svg>
        <span class="line"></span>
      </div>
      <div class="contact-text">@kerrlow_farm</div>
    </div>
  </section>
</body>
</html>
```